Stylish High End Wedding Videography/Films Website (BMTS)

We need a modern and high-end website look for our wedding video and films business. We films weddings all over the United Kingdom and at European destinations so need something to reflect our work. The website should be visually stunning with images and videos being the focal point as this is what our services are;

I have uploads of some items I like and the features the site needs to have. These have been taken from other websites using standout features.

We need the following pages;

1 - Homepage
2 - Films Index Page
3 - Individual Films Page
4 - Prices / Collection Page
5 - Reviews
6 - Options
7 - About
8 - Contact
9 - Blog Index
10 - Blog Page

All pages must be consistent so have a similar style.

Pages on menu:
Films
Prices
Reviews
Options
About
Contact

We require a responsive look too. Over 90% of our visitors access the website via their mobile devices.

Please use the colours from our logo to incorporate into the website.

Target Market(s)

Wedding Couples

Industry/Entity Type

Wedding Photography

Number of Pages Required

5+ page

Font styles to use
Sans Serif
Script

Requirements
Must have
• The logo must be in the centre of the menu at the top.

Social icons at the bottom of the page.

Use only two fonts including Lore which is supplied
Nice to have
• Different video for each page on the top header. This will play behind the menu.

```html
<!DOCTYPE html>
<html lang="en">
<head>
<meta charset="utf-8">
<title>BMTS — Wedding Films</title>
<link rel="stylesheet" href="https://fonts.googleapis.com/css2?family=Montserrat:wght@400;500;600;700;800&display=swap">
<style>
:root{
  --gold:#b0914f;
  --panel:#2a2627;
  --dark:#1c1819;
  --darker:#141112;
  --white:#ffffff;
  --muted:#a39c9d;
  --line:#3c3637;
}
*{margin:0;padding:0;box-sizing:border-box}
html,body{width:1200px;height:4134px;overflow:hidden}
body{position:relative;background:var(--darker);color:var(--white);font-family:'Montserrat',sans-serif}
.abs{position:absolute}
.photo{position:absolute}
/* hero */
.hero{left:0;top:0;width:1200px;height:650px;background:var(--panel)}
.hero-photo{left:459px;top:0;width:741px;height:650px;background:linear-gradient(160deg,#7a6a58 0%,#4d5a45 35%,#6f7478 60%,#3b3a35 100%)}
.brand{left:525px;top:22px;width:150px;text-align:center}
.brand-mark{display:block;margin:0 auto 6px;width:26px;height:26px;background:var(--gold)}
.brand-name{font-size:15px;font-weight:600;letter-spacing:3px;color:var(--white)}
.brand-sub{font-size:7px;letter-spacing:3px;color:var(--white);margin-top:3px}
.nav{top:50px;display:flex;align-items:center;gap:14px;font-size:12px;line-height:16px}
.nav-left{right:690px}
.nav-right{left:700px}
.nav a{color:var(--white);text-decoration:none}
.nav a.active{color:var(--gold)}
.nav .dot{width:4px;height:4px;border-radius:50%;background:var(--white)}
.btn-contact{left:932px;top:42px;width:114px;height:32px;border:1px solid var(--white);font-size:12px;display:flex;align-items:center;justify-content:center}
.counter{left:43px;top:312px;font-size:22px;font-weight:600}
.counter small{font-size:10px;color:var(--muted);font-weight:400}
.hero-title{left:266px;top:276px;font-size:50px;font-weight:700;color:transparent;-webkit-text-stroke:1.4px var(--white);letter-spacing:1px;white-space:nowrap}
.hero-sub{left:268px;top:338px;font-size:27px;font-weight:700;white-space:nowrap}
.link-more{font-size:11px;font-weight:600;letter-spacing:2px;border-left:1px solid var(--white);padding-left:16px;line-height:16px}
/* services */
.services{left:0;top:650px;width:1200px;height:999px;background:var(--dark)}
.h2{font-size:28px;font-weight:700}
.card{position:absolute;background:var(--panel)}
.card h3{color:var(--gold);font-size:18px;font-weight:700;line-height:22px}
.card p{font-size:12px;line-height:20px;color:var(--muted);margin:12px 0 22px}
.card .link-more{border-color:var(--gold)}
/* experience */
.experience{left:0;top:1649px;width:1200px;height:459px;background:linear-gradient(90deg,#2f2b2c,#3d3839 60%,#353031)}
.big-num{left:96px;top:1700px;font-size:340px;font-weight:800;color:#797374;letter-spacing:-8px;line-height:340px}
.lead{left:601px;top:1748px;width:446px;font-size:17px;line-height:26px}
.lead b{color:var(--gold);font-weight:600}
.body-small{left:601px;top:1846px;width:446px;font-size:11.5px;line-height:20px;color:var(--muted);text-align:justify}
/* projects */
.quote{left:280px;top:2828px;width:640px;text-align:center;font-size:18px;line-height:30px}
.quote sup{color:var(--gold);font-size:10px}
/* gallery */
.g-title{font-size:17px;font-weight:700}
.g-text{font-size:12px;line-height:20px;color:var(--muted)}
/* cta */
.cta{left:0;top:3710px;width:1200px;height:154px;background:var(--panel)}
.btn-gold{left:690px;top:3763px;width:189px;height:48px;background:var(--gold);font-size:12px;font-weight:600;display:flex;align-items:center;justify-content:center}
.foot-h{font-size:12px;font-weight:600;letter-spacing:2px}
.social{width:28px;height:28px;border-radius:50%;background:#3a3435}
</style>
</head>
<body>

<!-- hero -->
<section class="abs hero"></section>
<div class="photo hero-photo" role="img" aria-label="Bride and groom embracing beside a waterfall at sunset"></div>
<nav class="abs nav nav-left"><a class="active">Films</a><span class="dot"></span><a>Prices</a><span class="dot"></span><a>Reviews</a></nav>
<div class="abs brand"><span class="brand-mark"></span><div class="brand-name">BMTS</div><div class="brand-sub">WEDDING FILMS</div></div>
<nav class="abs nav nav-right"><a>Options</a><span class="dot"></span><a>About</a></nav>
<div class="abs btn-contact">Contact</div>
<svg class="abs" style="left:0;top:160px" width="160" height="330"><circle cx="0" cy="161" r="152" fill="none" stroke="#6b6465" stroke-dasharray="2 4"/><path d="M72 121l5-5 5 5M72 206l5 5 5-5" fill="none" stroke="#8c8586" stroke-width="1.2"/></svg>
<div class="abs counter">01 <small>/ 06</small></div>
<h1 class="abs hero-title">Unique Wedding</h1>
<div class="abs hero-sub">Video &amp; Photography</div>
<div class="abs link-more" style="left:268px;top:478px">WATCH VIDEO</div>

<!-- services -->
<section class="abs services"></section>
<h2 class="abs h2" style="left:152px;top:802px">What Can We Do</h2>
<div class="photo" style="left:818px;top:776px;width:114px;height:358px;background:linear-gradient(180deg,#6b5e52,#b79f8e 50%,#cbb9ad)" role="img" aria-label="Smiling bride"></div>
<div class="photo" style="left:601px;top:991px;width:217px;height:143px;background:linear-gradient(135deg,#7d6b6f,#8a5a6a 50%,#5e6a48)" role="img" aria-label="Wedding bouquet of dried flowers"></div>
<div class="photo" style="left:268px;top:903px;width:333px;height:359px;background:linear-gradient(135deg,#8c8174,#5a4e40 55%,#3e3830)" role="img" aria-label="Couple kissing surrounded by guests"></div>
<div class="photo" style="left:601px;top:1134px;width:331px;height:358px;background:linear-gradient(180deg,#9aa0a5,#4c4a4e 55%,#cfcfd2)" role="img" aria-label="Couple touching foreheads by the sea"></div>
<div class="card" style="left:536px;top:711px;width:282px;height:280px;padding:65px 50px 0 65px"><h3>Creative<br>Conceptions</h3><p>Sed do eiusmod tempor<br>incididunt ut labore<br>dolore magna ...</p><div class="link-more">MORE</div></div>
<div class="card" style="left:231px;top:1071px;width:229px;height:228px;padding:40px 30px 0 37px"><h3>Shooting &amp;<br>Editing</h3><p>Sed do eiusmod tempor<br>incididunt ut labore<br>dolore magna ...</p><div class="link-more">MORE</div></div>
<div class="card" style="left:563px;top:1302px;width:228px;height:227px;padding:38px 20px 0 38px"><h3>Unique<br>Photography</h3><p>Sed do eiusmod tempor<br>incididunt ut labore<br>dolore magna ...</p><div class="link-more">MORE</div></div>

<!-- experience -->
<section class="abs experience" role="img" aria-label="Faded photo of a wedding party outdoors"></section>
<div class="abs big-num">13</div>
<div class="abs h2" style="left:268px;top:1846px;line-height:32px">Years of Successful<br>experience</div>
<p class="abs lead">Sed ut perspiciatis <b>unde omnis iste natus</b> error sit voluptatem doloremque laudantium, <b>ipsa quae ab illo inventore</b> veritatis et quasi</p>
<p class="abs body-small">Nemo enim ipsam voluptatem quia voluptas sit aspernatur aut odit aut fugit, sed quia consequuntur magni dolores eos qui ratione voluptatem sequi nesciunt. Neque porro quisquam est, qui dolorem ipsum quia dolor sit amet, consectetur, adipisci velit, sed quia non numquam eius modi tempora incidunt ut labore et dolore magnam</p>
<div class="abs link-more" style="left:601px;top:1987px;color:var(--gold);border-color:var(--gold)">ABOUT US</div>

<!-- projects -->
<h2 class="abs h2" style="left:151px;top:2186px">Latest Projects</h2>
<svg class="abs" style="left:203px;top:2266px" width="16" height="24"><path d="M11 3L3 12l8 9" fill="none" stroke="#8c8586" stroke-width="1.5"/></svg>
<div class="photo" style="left:268px;top:2271px;width:664px;height:435px;background:linear-gradient(120deg,#3b3130,#6d6562 40%,#d8d3cf 60%,#4a3f3c)" role="img" aria-label="Newlyweds leaving the church under falling petals"></div>
<div class="abs" style="left:258px;top:2244px;font-size:50px;font-weight:700;line-height:60px;color:transparent;-webkit-text-stroke:1px #cfcaca;z-index:2">2</div>
<svg class="abs" style="left:540px;top:2428px" width="124" height="124"><circle cx="62" cy="62" r="60" fill="none" stroke="#fff" stroke-dasharray="2 4"/><path d="M52 46v32l26-16z" fill="none" stroke="#fff" stroke-width="2"/></svg>
<div class="abs" style="left:906px;top:2660px;font-size:52px;font-weight:700">4</div>
<svg class="abs" style="left:982px;top:2688px" width="16" height="24"><path d="M4 3l8 9-8 9" fill="none" stroke="#b0914f" stroke-width="1.5"/></svg>
<div class="abs" style="left:196px;top:2706px;transform:rotate(-90deg);transform-origin:0 0;font-size:18px;font-weight:700;white-space:nowrap"><span style="color:var(--gold)">03.</span> Amelia &amp; Sam Jordan</div>
<p class="abs quote"><sup>&ldquo;</sup> Sed ut perspiciatis unde omnis iste natus error sit voluptatem accusantium doloremque laudantium, totam rem aperiam, eaque ipsa quae ab illo inventore veritatis et quasi architecto beatae vitae dicta sunt explicabo <sup>&rdquo;</sup></p>
<svg class="abs" style="left:520px;top:2996px" width="160" height="30"><path d="M10 8l-6 7 6 7M150 8l6 7-6 7" fill="none" stroke="#8c8586" stroke-width="1.3"/></svg>
<div class="photo" style="left:570px;top:2981px;width:60px;height:60px;border-radius:50%;background:linear-gradient(135deg,#c8b8a8,#7a6558);border:2px solid #fff" role="img" aria-label="Portrait of reviewing couple"></div>
<div class="abs" style="left:500px;top:3051px;width:200px;text-align:center;color:var(--gold);font-size:13px;font-weight:600">Lena Marlow</div>

<!-- photography -->
<h2 class="abs h2" style="left:151px;top:3181px">Photography</h2>
<svg class="abs" style="left:68px;top:3374px" width="1068" height="24"><path d="M12 3L4 12l8 9M1056 3l8 9-8 9" fill="none" stroke="#b0914f" stroke-width="1.5"/></svg>
<div class="photo" style="left:152px;top:3246px;width:283px;height:281px;background:linear-gradient(135deg,#6e7a4e,#c9c2b6 55%,#3a3f4a)" role="img" aria-label="Laughing bride with groom outdoors"></div>
<div class="photo" style="left:459px;top:3246px;width:282px;height:281px;background:linear-gradient(135deg,#8a8a8a,#d4d4d4 50%,#505050)" role="img" aria-label="Black and white bride walking through smoke"></div>
<div class="photo" style="left:764px;top:3246px;width:283px;height:281px;background:linear-gradient(135deg,#a7b9c9,#6f8754 50%,#c7b09a)" role="img" aria-label="Couple embracing in a meadow with bouquet"></div>
<div class="abs" style="left:152px;top:3556px"><div class="g-title" style="color:var(--gold)">Ivy &amp; Tom</div><p class="g-text" style="margin-top:8px">Lorem Ipsum is simply dummy text<br>printing and typesettin</p></div>
<div class="abs" style="left:459px;top:3556px"><div class="g-title">Amelia &amp; Sam</div><p class="g-text" style="margin-top:8px">Lorem Ipsum is simply dummy text<br>printing and typesettin</p></div>
<div class="abs" style="left:764px;top:3556px"><div class="g-title">Ivy &amp; Tom</div><p class="g-text" style="margin-top:8px">Lorem Ipsum is simply dummy text<br>printing and typesettin</p></div>

<!-- call to action -->
<section class="abs cta"></section>
<div class="abs" style="left:293px;top:3768px;font-size:27px;font-weight:600">Start your project with us</div>
<div class="abs btn-gold">Get Started Now!</div>

<!-- footer -->
<div class="abs" style="left:152px;top:3950px;display:flex;align-items:center;gap:8px"><span style="width:14px;height:14px;background:var(--gold)"></span><span style="font-size:26px;font-weight:700;color:var(--gold)">BMTS</span></div>
<div class="abs" style="left:353px;top:3948px"><div class="foot-h">CONTACT US</div><div style="margin-top:16px;font-size:18px">Call. <span style="color:var(--gold)">+1 800 555 0199</span></div><div style="margin-top:6px;font-size:12px;color:var(--muted)">e. hello@bmtsfilms.com</div></div>
<div class="abs" style="left:646px;top:3948px"><div class="foot-h">GET IN TOUCH</div><div style="margin-top:16px;font-size:18px;color:var(--muted)">Studio 8 Elm Arcade,</div><div style="margin-top:6px;font-size:12px;color:var(--muted)">Harrow Lane, Leeds LS2 7QD</div></div>
<svg class="abs" style="left:1026px;top:3950px" width="20" height="26"><path d="M10 24V3M3 10l7-7 7 7" fill="none" stroke="#b0914f" stroke-width="1.5"/></svg>
<div class="abs" style="left:75px;top:4070px;width:1048px;height:1px;background:var(--line)"></div>
<div class="abs" style="left:152px;top:4097px;font-size:10px;color:var(--muted)">2020 © BMTS Wedding Films. All Rights Reserved.</div>
<div class="abs" style="left:902px;top:4089px;display:flex;gap:10px"><span class="social"></span><span class="social"></span><span class="social"></span><span class="social"></span></div>

</body>
</html>
```